CalmPeak Nurses' Manifesto

Design a manifesto to inspire and motivate nurses to work at minimum standards of excellence in their nursing practice.

The manifesto will become a feature of our website, at conferences, workshops and retreats. It will also be featured on other marketing tools.

Primary Market:
Nurses and/or other healthcare professionals (specifically Doctors, Occupational Therapists, Psychologists and Social Workers).

However the manifesto is equally applicable to all nurses and healthcare professionals from new graduates to very experienced senior clinicians, administration officers,managers and healthcare executive personnel.

Mainly females and primarily 35 to 65 years old, which suggests people in this target age group have extensive experience, but have become jaded'.

The purpose of our business is to assist healthcare professionals, primarily nurses, to maintain their enthusiasm and excellence in service provision, for their benefit as well as the benefit of the clients.

I have attached:
File 1: Copy Samples and examples: which has the copy for the manifesto, examples that appeal to us and our 3 attempts.
File 2: Our colour Spec Sheet, HOWEVER the colours are not necessary limited to these colours. These colours are not in the logo that will be on the manifesto. The colours on the logo attached can/or also be used.
File 3: Prototype logo. The final logo will be available within 3 to 4 days.

Industry/Entity Type

Healthcare

Requirements
Must have
• Must use the copy as per the attached file.

It should be contemporary, eye catching and motivational.

Should not have
• MUST BE EASY TO READ. Each line MUST be clearly defined from each other.

```html
<!DOCTYPE html>
<html lang="en">
<head>
<meta charset="utf-8">
<title>CalmPeak Nurses' Manifesto</title>
<link rel="stylesheet" href="https://fonts.googleapis.com/css2?family=Anton&family=Arimo:wght@700&family=Bebas+Neue&family=Rokkitt:wght@700&display=swap">
<style>
  :root {
    --teal-deep: #3a6461;
    --teal-mid: #4b7572;
    --lime: #9dc33b;
    --chalk: #f2f2ee;
  }
  html, body {
    margin: 0;
    padding: 0;
    overflow: hidden;
    background: var(--teal-deep);
  }
  .manifesto {
    position: relative;
    width: 811px;
    height: 1200px;
    overflow: hidden;
    background: var(--teal-mid);
  }
  .texture {
    position: absolute;
    inset: 0;
    background:
      radial-gradient(ellipse 340px 260px at 300px 240px, rgba(160,185,180,0.45), transparent 70%),
      radial-gradient(ellipse 300px 380px at 640px 620px, rgba(150,178,172,0.35), transparent 70%),
      radial-gradient(ellipse 280px 220px at 200px 1000px, rgba(120,150,146,0.3), transparent 70%),
      linear-gradient(180deg, var(--teal-mid) 0%, var(--teal-deep) 100%);
  }
  .line {
    position: absolute;
    margin: 0;
    line-height: 1;
    white-space: nowrap;
    color: var(--chalk);
  }
  .condensed { font-family: "Bebas Neue", "Oswald", sans-serif; font-weight: 400; }
  .heavy { font-family: "Anton", "Impact", sans-serif; font-weight: 400; }
  .slab { font-family: "Rokkitt", "Rockwell", serif; font-weight: 700; }
  .lime { color: var(--lime); }
  .vertical-down { writing-mode: vertical-rl; }
  .vertical-up { writing-mode: vertical-rl; transform: rotate(180deg); }

  .title {
    position: absolute;
    top: 6px;
    left: 0;
    width: 662px;
    text-align: center;
    margin: 0;
    font-family: "Arimo", "Arial", sans-serif;
    font-weight: 700;
    font-size: 26px;
    line-height: 1.1;
    color: var(--chalk);
  }

  .brand {
    position: absolute;
    left: 590px;
    top: 1075px;
    width: 221px;
    display: flex;
    flex-direction: column;
    align-items: center;
    gap: 12px;
  }
  .brand-dot {
    width: 34px;
    height: 34px;
    border-radius: 50%;
    background: var(--lime);
  }
  .brand-name {
    font-family: "Bebas Neue", "Oswald", sans-serif;
    font-size: 36px;
    line-height: 1;
    color: var(--chalk);
  }
</style>
</head>
<body>
<main class="manifesto">
  <div class="texture" role="img" aria-label="Weathered dark teal grunge texture background"></div>

  <h1 class="title">Nurses' Manifesto</h1>

  <p class="line condensed lime" style="top:54px;left:74px;font-size:80px;letter-spacing:13px;">LIVE YOUR DREAM</p>
  <p class="line condensed" style="top:128px;left:74px;font-size:58px;letter-spacing:0.5px;">ONLY FOLLOW EXCEPTIONAL LEADERS</p>
  <p class="line condensed" style="top:196px;left:74px;font-size:34px;letter-spacing:2px;">ALWAYS LEAD WITH PURPOSE</p>
  <p class="line condensed" style="top:228px;left:74px;font-size:34px;letter-spacing:1.6px;">PASSION AND COMMITMENT</p>

  <p class="line condensed" style="top:198px;left:446px;font-size:76px;letter-spacing:4px;">ALWAYS</p>
  <p class="line condensed" style="top:270px;left:446px;font-size:56px;letter-spacing:0px;">BE SOLUTION</p>
  <p class="line condensed" style="top:318px;left:446px;font-size:76px;letter-spacing:2px;">FOCUSED</p>

  <p class="line condensed vertical-down" style="top:203px;left:648px;font-size:76px;letter-spacing:-1px;">SEEK SUCCESS FIRSTLY FROM WITHIN</p>

  <p class="line condensed lime" style="top:282px;left:62px;font-size:150px;letter-spacing:-2px;">YOU ARE</p>
  <p class="line heavy" style="top:388px;left:66px;font-size:100px;letter-spacing:1px;">UNIQUE</p>
  <p class="line slab lime" style="top:410px;left:442px;font-size:28px;">REVEL IN YOUR</p>
  <p class="line slab lime" style="top:457px;left:442px;font-size:27px;">INDIVIDUALITY.</p>

  <p class="line condensed vertical-up" style="top:518px;left:72px;font-size:66px;letter-spacing:14px;">ALWAYS</p>
  <p class="line condensed" style="top:524px;left:162px;font-size:40px;letter-spacing:2.5px;">DO THE RIGHT</p>
  <p class="line condensed lime" style="top:562px;left:160px;font-size:118px;letter-spacing:0px;">THING</p>
  <p class="line condensed" style="top:684px;left:162px;font-size:40px;letter-spacing:-0.5px;">WITHOUT EXCEPTION</p>

  <p class="line heavy" style="top:490px;left:386px;font-size:90px;letter-spacing:2px;">TRUST</p>
  <p class="line condensed" style="top:586px;left:386px;font-size:46px;letter-spacing:0px;">YOUR KNOWLEDGE</p>
  <p class="line condensed" style="top:638px;left:386px;font-size:44px;letter-spacing:1px;">AND SEEK ADVICE</p>
  <p class="line heavy lime" style="top:672px;left:405px;font-size:86px;letter-spacing:9px;">ONLY</p>

  <p class="line heavy" style="top:750px;left:72px;font-size:90px;letter-spacing:-5px;">CELEBRATE</p>
  <p class="line condensed" style="top:773px;left:405px;font-size:32px;letter-spacing:-1.2px;">FROM RESPECTED SOURCES</p>
  <p class="line condensed" style="top:811px;left:405px;font-size:32px;letter-spacing:-0.3px;">RESPECT AND VALUE THE</p>
  <p class="line heavy" style="top:849px;left:72px;font-size:62px;letter-spacing:2px;">DIVERSITY</p>
  <p class="line heavy" style="top:849px;left:392px;font-size:64px;letter-spacing:3px;">SUPPORT</p>

  <p class="line condensed lime" style="top:920px;left:74px;font-size:34px;letter-spacing:2.5px;">OF AUSTRALIAN CULTURE</p>
  <p class="line condensed" style="top:922px;left:396px;font-size:28px;letter-spacing:-0.5px;">YOUR COLLEAGUES</p>
  <p class="line heavy" style="top:912px;left:541px;font-size:42px;letter-spacing:5px;">AND</p>
  <p class="line condensed" style="top:968px;left:541px;font-size:22px;letter-spacing:6px;">THEIR</p>
  <p class="line condensed" style="top:994px;left:541px;font-size:22px;letter-spacing:2px;">PURPOSE</p>
  <p class="line slab vertical-up" style="top:968px;left:500px;font-size:40px;letter-spacing:2px;">CHAMPION</p>

  <p class="line condensed" style="top:963px;left:74px;font-size:34px;">BE</p>
  <p class="line condensed" style="top:1003px;left:74px;font-size:34px;">A</p>
  <p class="line condensed" style="top:1044px;left:74px;font-size:34px;">LIFELONG</p>
  <p class="line condensed" style="top:1085px;left:74px;font-size:34px;">LEARNER</p>
  <p class="line condensed lime" style="top:950px;left:134px;font-size:115px;letter-spacing:-2px;">LEARN</p>
  <p class="line condensed" style="top:966px;left:351px;font-size:40px;">SOMETHING</p>
  <p class="line condensed" style="top:1016px;left:351px;font-size:34px;letter-spacing:0px;">NEW EACH DAY</p>

  <p class="line heavy lime" style="top:1056px;left:214px;font-size:84px;letter-spacing:-3px;">DELIVER</p>
  <p class="line condensed" style="top:1152px;left:212px;font-size:40px;letter-spacing:1px;">CARE SKILLFULLY</p>

  <div class="brand">
    <span class="brand-dot"></span>
    <span class="brand-name">CalmPeak</span>
  </div>
</main>
</body>
</html>
```